Truck Sign Writing Design

Looking for some help with designing the sign writing to go on our small truck. We have our company logos already. Our truck is fitted with black acm panels on the sides ready to go. The trucks cab is currently getting repainted white - the black side panels will remain with black showing and the sign writing will be put over the top - Black will remain being the background colour) (Please incorporate this into your design)
. Would like to get designs on the front of the truck, both doors, and each side panels. The services we provide are Tree Removal, Tree Pruning, and Stump Grinding, which may be incorporated into the design.
Ideally we would like our logo, our services (as above), phone number 027963214 and possibly website (www.birchlinearbor.co.nz) on the truck. This may or may not be needed in all areas. etc front of truck. Open to ideas and Suggestions.
Design must include Illustrator .AI file.
Company colours black and green (#5b842b)
Attached is our truck and example of the front (another truck).
Font used is - Trajan Pro Bold

Look and feel
Each slider illustrates characteristics of the customer's brand and the style your logo design should communicate.

```html
<!DOCTYPE html>
<html lang="en">
<head>
<meta charset="utf-8">
<title>Birchline Arbor – Truck Side Panels</title>
<link rel="stylesheet" href="https://fonts.googleapis.com/css2?family=Cinzel:wght@400;700&display=swap">
<style>
  :root {
    --brand-green: #5b9e12;
    --backdrop-green: #4ba300;
    --panel-black: #000000;
    --text-white: #ffffff;
    --leaf-shade: #0f2a0c;
  }
  * { margin: 0; padding: 0; box-sizing: border-box; }
  html, body { width: 1200px; height: 849px; overflow: hidden; }
  body {
    background: var(--backdrop-green);
    font-family: "Cinzel", "Times New Roman", serif;
    position: relative;
  }
  .side-panel {
    position: absolute;
    top: 227px;
    width: 540px;
    height: 395px;
    background: var(--panel-black);
    box-shadow: 4px 4px 6px rgba(0, 0, 0, 0.35);
    overflow: hidden;
    text-align: center;
  }
  .side-panel--contact { left: 40px; }
  .side-panel--services { left: 620px; }

  .leaf-decoration {
    position: absolute;
    border-radius: 50%;
    background: radial-gradient(ellipse at center, var(--leaf-shade) 0%, rgba(15, 42, 12, 0) 70%);
  }
  .side-panel--contact .leaf-decoration { right: 20px; top: 195px; width: 170px; height: 190px; }
  .side-panel--services .leaf-decoration { left: 40px; top: 215px; width: 150px; height: 160px; }

  .brand-mark {
    position: absolute;
    left: 50%;
    transform: translateX(-50%);
    border: 4px solid var(--brand-green);
    border-radius: 50%;
  }
  .side-panel--contact .brand-mark { top: 45px; width: 128px; height: 128px; }
  .side-panel--services .brand-mark { top: 43px; width: 110px; height: 110px; }

  .brand-name {
    position: absolute;
    left: 0; right: 0;
    color: var(--brand-green);
    font-weight: 700;
    letter-spacing: 0.06em;
    line-height: 1;
  }
  .side-panel--contact .brand-name { top: 185px; font-size: 34px; }
  .side-panel--services .brand-name { top: 162px; font-size: 30px; }

  .call-badge {
    position: absolute;
    left: 50%;
    top: 256px;
    transform: translateX(-50%);
    background: var(--brand-green);
    color: var(--text-white);
    font-weight: 700;
    font-size: 15px;
    line-height: 18px;
    padding: 0 6px;
  }
  .phone-number {
    position: absolute;
    left: 0; right: 0;
    font-weight: 400;
    line-height: 1;
  }
  .side-panel--contact .phone-number { top: 278px; font-size: 40px; color: var(--text-white); }
  .side-panel--services .phone-number { top: 290px; font-size: 34px; color: var(--brand-green); }

  .service-list {
    position: absolute;
    left: 0; right: 0;
    top: 220px;
    color: var(--text-white);
    font-weight: 700;
    font-size: 21px;
    line-height: 28px;
    list-style: none;
  }
  .website {
    position: absolute;
    left: 0; right: 0;
    color: var(--text-white);
    font-size: 11px;
    letter-spacing: 0.02em;
  }
  .side-panel--contact .website { top: 338px; }
  .side-panel--services .website { top: 341px; }
</style>
</head>
<body>
  <section class="side-panel side-panel--contact" aria-label="Truck left side panel">
    <div class="leaf-decoration" role="img" aria-label="Decorative dark green leaves"></div>
    <div class="brand-mark"></div>
    <h1 class="brand-name">BIRCHLINE ARBOR</h1>
    <span class="call-badge">CALL</span>
    <p class="phone-number">027-963-214</p>
    <p class="website">WWW.BIRCHLINEARBOR.CO.NZ</p>
  </section>

  <section class="side-panel side-panel--services" aria-label="Truck right side panel">
    <div class="leaf-decoration" role="img" aria-label="Decorative dark green leaves"></div>
    <div class="brand-mark"></div>
    <h2 class="brand-name">BIRCHLINE ARBOR</h2>
    <ul class="service-list">
      <li>TREE REMOVAL &nbsp;•&nbsp; TREE PRUNING</li>
      <li>STUMP GRINDING</li>
    </ul>
    <p class="phone-number">027-963-214</p>
    <p class="website">WWW.BIRCHLINEARBOR.CO.NZ</p>
  </section>
</body>
</html>
```